Vital Spark Electrical in need of a business card design

We need a new business card designed for our electrical business. We have a logo already which I will attach below.
Would like the business card to be..
-BLACK background preferably, possibly white back ground behind logo if colours clash.
-White & Blue (logo blue) text
Something that makes the logo pop, & a modern look. Possibly minimal clean format.

REQUIRE:
-Logo on front & back

TEXT TO INCLUDE (ON ONE SIDE):

Tom Harlow
Director/Electrician
M: 0417 365 208
E:info@vitalsparkelectrical-example.com.au
W:www.vitalsparkelectrical-example.com.au
R.E.C 57318

Custom/New Homes
Renovations
Commercial Office/Shop Fit-outs
Communications & Security Cameras
Electric Vehicle Chargers
Airconditioning
Updates

Requirements
Nice to have
• Possibly even lighten the grey shades for the words 'Vital' & 'Spark' to be more easily read on a black background.

```html
<!DOCTYPE html>
<html lang="en">
<head>
<meta charset="utf-8">
<title>Vital Spark Electrical – Business Card</title>
<link href="https://fonts.googleapis.com/css2?family=Roboto:ital,wght@0,400;0,500;1,400;1,700&display=swap" rel="stylesheet">
<style>
  :root {
    --page: #5b5b5b;
    --card: #232323;
    --card-edge: #1b1b1b;
    --blue: #1a9ad6;
    --white: #f2f2f2;
    --grey: #a9b4bf;
  }
  * { box-sizing: border-box; margin: 0; padding: 0; }
  html, body { width: 1200px; height: 1021px; overflow: hidden; }
  body {
    background: var(--page);
    font-family: "Roboto", Arial, sans-serif;
    color: var(--white);
    position: relative;
  }
  .card {
    position: absolute;
    left: 280px;
    width: 640px;
    height: 391px;
    background: var(--card);
    border: 1px solid var(--card-edge);
    box-shadow: 0 10px 30px rgba(0,0,0,.35);
    overflow: hidden;
  }
  .card--front { top: 70px; }
  .card--back { top: 560px; }

  .wordmark {
    display: flex;
    align-items: center;
    gap: 12px;
    font-weight: 500;
    color: var(--grey);
    letter-spacing: .5px;
    white-space: nowrap;
  }
  .wordmark__square { width: 18px; height: 18px; background: var(--blue); flex: none; }
  .card--front .wordmark {
    position: absolute; left: 0; right: 0; top: 172px;
    justify-content: center; font-size: 36px;
  }
  .card--back .wordmark {
    position: absolute; right: 40px; top: 70px; font-size: 26px;
  }
  .card--back .wordmark__square { width: 14px; height: 14px; }

  .tab {
    position: absolute; left: 0; top: 58px;
    width: 12px; height: 46px;
    background: var(--blue);
    border-radius: 0 8px 8px 0;
  }
  .contact { position: absolute; left: 56px; top: 58px; }
  .contact__name { font-size: 23px; font-weight: 700; font-style: italic; color: var(--blue); }
  .contact__role { font-size: 17px; font-style: italic; margin-top: 2px; }
  .contact__licence { font-size: 17px; font-style: italic; margin-top: 26px; }
  .contact__list { list-style: none; margin-top: 30px; font-size: 16px; line-height: 24px; }
  .contact__list li { display: flex; align-items: center; gap: 8px; }
  .contact__list svg { width: 15px; height: 15px; flex: none; }

  .services {
    position: absolute; right: 22px; bottom: 40px;
    list-style: none; text-align: right;
    font-size: 17px; line-height: 24px;
  }
  .services li { display: flex; justify-content: flex-end; align-items: center; gap: 14px; }
  .services li::after {
    content: ""; width: 30px; height: 7px; background: var(--blue);
    transform: skewX(-20deg); flex: none;
  }
</style>
</head>
<body>
  <section class="card card--front" aria-label="Card front">
    <div class="wordmark"><span class="wordmark__square"></span>Vital Spark Electrical</div>
  </section>

  <section class="card card--back" aria-label="Card back">
    <div class="tab"></div>
    <div class="contact">
      <p class="contact__name">Tom Harlow</p>
      <p class="contact__role">Director/Electrician</p>
      <p class="contact__licence">R.E.C 57318</p>
      <ul class="contact__list">
        <li>
          <svg viewBox="0 0 16 16" aria-hidden="true"><path d="M4 1.5l2.2 2.8-1.3 1.6c.9 2 2.4 3.5 4.4 4.4l1.6-1.3 2.8 2.2-1.4 2.3C7.6 13 3 8.4 2.5 3z" fill="none" stroke="#1a9ad6" stroke-width="1.4" stroke-linejoin="round"/></svg>
          0417 365 208
        </li>
        <li>
          <svg viewBox="0 0 16 16" aria-hidden="true"><rect x="1.5" y="3.5" width="13" height="9" fill="none" stroke="#1a9ad6" stroke-width="1.4"/><path d="M1.5 3.5L8 9l6.5-5.5" fill="none" stroke="#1a9ad6" stroke-width="1.4"/></svg>
          info@vitalsparkelectrical-example.com.au
        </li>
        <li>
          <svg viewBox="0 0 16 16" aria-hidden="true"><g fill="none" stroke="#1a9ad6" stroke-width="1.2"><circle cx="8" cy="8" r="6.5"/><ellipse cx="8" cy="8" rx="3" ry="6.5"/><path d="M1.5 8h13M2.6 4.6h10.8M2.6 11.4h10.8"/></g></svg>
          www.vitalsparkelectrical-example.com.au
        </li>
      </ul>
    </div>

    <div class="wordmark"><span class="wordmark__square"></span>Vital Spark Electrical</div>

    <ul class="services">
      <li>Custom/New Homes</li>
      <li>Renovations</li>
      <li>Commercial Office/Shop Fit-outs</li>
      <li>Communications &amp; Security Cameras</li>
      <li>Electric Vehicle Chargers</li>
      <li>Airconditioning</li>
    </ul>
  </section>
</body>
</html>
```